Web design for software company

I'm a software developer that designs high end specialist web applications, mobile apps and user friendly applications for medium to large customers. I integrate different systems together within a company and provide web based applications or mobile apps to view and edit information in that web of linked systems.

I currently work alone, basically selling my time on specialist projects, but also build my own software solutions which I eventually want to put into the market.

My company name is Quarrymind (lowercase 'L' for logic) and I work from the Netherlands. I've attached my current logo which is basically just text in VOXbox font. Current colours are mustard yellow and grey, but i'm open to other options to better fit the web design.

I've got a sort of slogan: "Specialized software development" - better ideas are welcome. The slogan in the logo attachment is older.

I'm looking for a site design that reflects my work as being on the cutting edge of technology, but being clear and simple. My thinking with the name Quarrymind is that it refers to the underlying mechanism and logic of software.

The site will not be text heavy, so some kind of large graphic to do with software design is welcome. I expect about 4 or 5 main pages or sections of the site in which i'll eventually add things like a blog or contact info etc.

Industry/Entity Type

It Company

Number of Pages Required

1 page

Font styles to use
Sans Serif

Requirements
Nice to have
• A large graphic or photo relevant to my focus as a software developer. Something that shows connecting of software systems with perhaps a variety of devices/browsers that would display data from that cloud of systems.
• Something like these (allthough these are ugly - but the idea is what i mean):
• http://st4.pixelvaultimg.example/2000817/22458/i/450/pixelvaultimg_224581193-Cloud-computing-user-interface.jpg
• http://business.tallwick.example/images/modules/mobile-device-policy-design-banner.png
• https://www.pagecrafta.example/images/responsive-web-design.jpg
• http://www.brevanto.example/images/web_apps.png
• https://www.keymurra.example/assets/img/product/web-app@2x.png?v2
Should not have
• Photographs of smiling happy people looking at a screen that make it look like it's a huge business with many offices. I'm a one-man company which could perhaps grow a little bit, but i want to focus on my expertise instead of size.

```html
<!DOCTYPE html>
<html lang="en">
<head>
<meta charset="utf-8">
<title>Quarrymind — Software Development</title>
<link rel="stylesheet" href="https://fonts.googleapis.com/css2?family=Lato:wght@700;900&family=Open+Sans:wght@300;400;600;700&display=swap">
<style>
  :root {
    --green: #3aae6f;
    --navy: #0e4a70;
    --orange: #f47a20;
    --grey-band: #ebebeb;
    --text: #555555;
    --dark: #2b2b2b;
    --white: #ffffff;
  }
  * { box-sizing: border-box; margin: 0; padding: 0; }
  html, body { width: 1200px; height: 2695px; overflow: hidden; }
  body { font-family: "Open Sans", Arial, sans-serif; color: var(--text); background: var(--white); }
  .container { width: 1046px; margin: 0 auto; position: relative; height: 100%; }

  /* top bar */
  .topbar { height: 41px; background: var(--green); color: var(--white); }
  .topbar .container { display: flex; align-items: center; justify-content: space-between; }
  .social-mini { display: flex; gap: 16px; }
  .social-mini span { width: 14px; height: 14px; border-radius: 50%; background: var(--white); opacity: .9; }
  .callus { font-size: 21px; font-weight: 400; display: flex; align-items: center; gap: 8px; letter-spacing: .2px; }
  .callus svg { width: 20px; height: 20px; }

  /* header */
  .header { height: 105px; background: var(--white); box-shadow: 0 2px 4px rgba(0,0,0,.08); position: relative; z-index: 2; }
  .header .container { display: flex; align-items: center; justify-content: space-between; }
  .brand { display: flex; align-items: center; gap: 14px; }
  .brand-square { width: 38px; height: 38px; background: var(--navy); }
  .brand-name { font-size: 34px; font-weight: 400; color: var(--navy); letter-spacing: .5px; }
  .nav { display: flex; align-items: center; gap: 0; }
  .nav a { text-decoration: none; font-size: 19px; color: #8a8a8a; padding: 13px 22px; text-transform: uppercase; }
  .nav a.active { background: var(--orange); color: var(--white); padding: 13px 19px; margin-right: 2px; }

  /* hero */
  .hero { height: 572px; position: relative;
    background: linear-gradient(100deg, #4a5560 0%, #6b7884 45%, #3e5a70 75%, #2d4252 100%); }
  .hero-photo { position: absolute; inset: 0; }
  .hero-title { position: absolute; left: 0; top: 170px; font-family: "Lato", Arial, sans-serif; font-weight: 900;
    font-size: 54px; line-height: 72px; color: var(--white); letter-spacing: .3px; }
  .btn-outline-light { position: absolute; left: 0; top: 344px; width: 174px; height: 56px; border: 2px solid var(--white);
    border-radius: 3px; color: var(--white); font-family: "Lato", Arial, sans-serif; font-weight: 700; font-size: 21px;
    display: flex; align-items: center; justify-content: center; }
  .quote-form { position: absolute; right: 0; top: 120px; width: 365px; height: 413px; background: rgba(25,70,100,.85); padding: 0 15px; }
  .quote-form h3 { margin: 0 -15px; height: 48px; background: var(--white); color: var(--orange); font-weight: 400;
    font-size: 25px; display: flex; align-items: center; justify-content: center; }
  .field { background: var(--white); height: 41px; margin-top: 16px; font-size: 15px; color: #777; padding: 10px 14px; }
  .field.message { height: 93px; }
  .btn-submit { display: block; margin: 16px auto 0; width: 144px; height: 45px; background: var(--green); color: var(--white);
    font-size: 20px; display: flex; align-items: center; justify-content: center; }

  /* section titles */
  .section-title { font-size: 47px; font-weight: 300; color: var(--navy); text-align: center; letter-spacing: .5px; }
  .section-title em { font-style: normal; color: var(--green); }

  /* services */
  .services { height: 500px; background: var(--grey-band); padding-top: 52px; }
  .services .lead { width: 800px; margin: 14px auto 0; text-align: center; font-size: 16px; line-height: 25px; }
  .service-list { display: flex; justify-content: space-between; margin-top: 28px; padding: 0 0 0 0; }
  .service { width: 265px; text-align: center; }
  .service-icon { width: 126px; height: 126px; border-radius: 50%; background: var(--navy); margin: 0 auto;
    display: flex; align-items: center; justify-content: center; }
  .service-icon svg { width: 64px; height: 64px; }
  .service h4 { font-size: 23px; font-weight: 400; margin-top: 14px; }
  .service h4.green { color: var(--green); }
  .service h4.orange { color: var(--orange); }
  .service p { font-size: 15.5px; line-height: 25px; margin-top: 10px; }

  /* welcome */
  .welcome { height: 402px; background: var(--white); }
  .welcome-copy { position: absolute; left: 0; top: 60px; width: 590px; }
  .welcome-copy h2 { font-size: 48px; font-weight: 300; color: var(--navy); letter-spacing: .5px; white-space: nowrap; }
  .welcome-copy h2 em { font-style: normal; color: var(--green); }
  .welcome-copy p { font-size: 16px; line-height: 25px; margin-top: 8px; }
  .btn-outline-navy { margin-top: 38px; width: 174px; height: 58px; border: 2px solid var(--navy); border-radius: 3px;
    color: var(--navy); font-size: 23px; display: flex; align-items: center; justify-content: center; }
  .welcome-visual { position: absolute; right: 0; top: 57px; width: 415px; height: 334px;
    background: linear-gradient(180deg, #1a1a1a 0%, #2a2a2a 62%, #c9c9c9 62%, #a9a9a9 80%, #e2e2e2 100%); border-radius: 6px; }

  /* work */
  .work { height: 469px; background: var(--grey-band); padding-top: 38px; }
  .work-grid { display: flex; justify-content: space-between; margin-top: 26px; }
  .work-card { width: 234px; height: 296px; background: var(--white); }
  .work-image { height: 145px; }
  .work-card h5 { font-size: 17px; font-weight: 400; color: var(--green); line-height: 25px; padding: 8px 6px 0; }
  .work-card p { font-size: 14.5px; line-height: 25px; padding: 4px 6px 0; }

  /* testimonials */
  .clients { height: 302px; background: var(--white); padding-top: 52px; }
  .client-list { display: flex; margin-top: 26px; }
  .client { display: flex; width: 553px; gap: 22px; }
  .client-photo { width: 126px; height: 126px; border-radius: 50%; border: 2px solid var(--green); flex: none; }
  .client p { font-size: 15.5px; line-height: 25px; width: 345px; }
  .client .name { display: block; font-weight: 700; color: var(--navy); margin-top: 4px; }

  /* footer */
  .footer { height: 304px; background: var(--dark); text-align: center; padding-top: 46px; }
  .footer-brand { display: inline-flex; align-items: center; gap: 12px; }
  .footer-brand .brand-square { background: var(--green); width: 32px; height: 32px; }
  .footer-brand .brand-name { color: var(--white); font-size: 30px; }
  .footer-social { display: flex; justify-content: center; gap: 24px; margin-top: 30px; }
  .footer-social span { width: 50px; height: 50px; border-radius: 50%; border: 2px solid var(--white); }
  .footer-social span.first { border-color: var(--green); }
  .footer-links { margin-top: 18px; font-size: 15px; color: var(--white); }
  .footer-links a { color: var(--white); text-decoration: none; }
  .footer-links a.active { color: var(--green); }
  .footer-links .sep { margin: 0 8px; }
  .copyright { margin-top: 18px; font-size: 15px; color: var(--white); }
  .copyright span { color: var(--green); }
</style>
</head>
<body>

<div class="topbar">
  <div class="container">
    <div class="social-mini"><span></span><span></span><span></span></div>
    <div class="callus">CALL US NOW
      <svg viewBox="0 0 24 24" fill="#fff"><path d="M6.6 10.8c1.4 2.8 3.8 5.1 6.6 6.6l2.2-2.2c.3-.3.7-.4 1-.2 1.1.4 2.3.6 3.6.6.6 0 1 .4 1 1V20c0 .6-.4 1-1 1C10.6 21 3 13.4 3 4c0-.6.4-1 1-1h3.5c.6 0 1 .4 1 1 0 1.3.2 2.5.6 3.6.1.3 0 .7-.2 1l-2.3 2.2z"/></svg>
      020 555 0147</div>
  </div>
</div>

<header class="header">
  <div class="container">
    <div class="brand"><span class="brand-square"></span><span class="brand-name">QUARRYMIND</span></div>
    <nav class="nav">
      <a class="active">Home</a><a>About</a><a>Services</a><a>Our Work</a><a>News</a><a>Contact</a>
    </nav>
  </div>
</header>

<section class="hero">
  <div class="hero-photo" role="img" aria-label="Desk scene with a tablet showing business charts, glasses and a pen"></div>
  <div class="container">
    <h1 class="hero-title">MODERN, USER<br>FRIENDLY SOFTWARE</h1>
    <div class="btn-outline-light">VIEW MORE</div>
    <form class="quote-form">
      <h3>GET A FREE QUOTE</h3>
      <div class="field">Enter Name</div>
      <div class="field">Enter Email</div>
      <div class="field">Enter Contact No.</div>
      <div class="field message">Enter Message</div>
      <div class="btn-submit">SUBMIT</div>
    </form>
  </div>
</section>

<section class="services">
  <div class="container">
    <h2 class="section-title">SERVICES <em>WE PROVIDE</em></h2>
    <p class="lead">Lorem Ipsum is simply dummy text of the printing and typesetting industry. Lorem Ipsum has been the industry's standard dummy text ever since the 1500.</p>
    <div class="service-list">
      <div class="service">
        <div class="service-icon"><svg viewBox="0 0 64 64" fill="#fff"><rect x="6" y="10" width="52" height="34" rx="3"/><rect x="11" y="15" width="42" height="24" fill="#0e4a70"/><rect x="27" y="44" width="10" height="7"/><rect x="18" y="51" width="28" height="4" rx="1"/></svg></div>
        <h4 class="green">Web Development</h4>
        <p>Lorem Ipsum is simply dummy text of the printing and typesetting industry.</p>
      </div>
      <div class="service">
        <div class="service-icon"><svg viewBox="0 0 64 64" fill="#fff"><rect x="19" y="6" width="26" height="52" rx="4"/><rect x="22" y="13" width="20" height="35" fill="#0e4a70"/><circle cx="32" cy="53" r="2.5" fill="#0e4a70"/></svg></div>
        <h4 class="orange">Mobile Apps</h4>
        <p>Lorem Ipsum is simply dummy text of the printing and typesetting industry.</p>
      </div>
      <div class="service">
        <div class="service-icon"><svg viewBox="0 0 64 64" fill="#fff"><path d="M12 20h12a6 6 0 1 1 10 0h12v12a6 6 0 1 1 0 10v12H34a6 6 0 1 0-10 0H12V42a6 6 0 1 0 0-10z"/></svg></div>
        <h4 class="orange">Systems Integration</h4>
        <p>Lorem Ipsum is simply dummy text of the printing and typesetting industry.</p>
      </div>
      <div class="service">
        <div class="service-icon"><svg viewBox="0 0 64 64" fill="#fff"><circle cx="32" cy="20" r="8"/><circle cx="15" cy="25" r="6"/><circle cx="49" cy="25" r="6"/><path d="M18 50c0-10 6-16 14-16s14 6 14 16z"/><path d="M4 46c0-7 5-12 11-12 3 0 5 1 6 2-3 3-5 7-5 10z"/><path d="M60 46c0-7-5-12-11-12-3 0-5 1-6 2 3 3 5 7 5 10z"/></svg></div>
        <h4 class="orange">User Friendly</h4>
        <p>Lorem Ipsum is simply dummy text of the printing and typesetting industry.</p>
      </div>
    </div>
  </div>
</section>

<section class="welcome">
  <div class="container">
    <div class="welcome-copy">
      <h2>WELCOME TO <em>QUARRYMIND</em></h2>
      <p>Lorem Ipsum is simply dummy text of the printing and typesetting industry. Lorem Ipsum has been the industry's standard dummy text ever since the 1500s, when an unknown printer took a galley of type and scrambled it to make a type specimen book.</p>
      <div class="btn-outline-navy">READ MORE</div>
    </div>
    <div class="welcome-visual" role="img" aria-label="Desktop monitor displaying the company name"></div>
  </div>
</section>

<section class="work">
  <div class="container">
    <h2 class="section-title">OUR <em>WORK</em></h2>
    <div class="work-grid">
      <article class="work-card">
        <div class="work-image" role="img" aria-label="Hands holding a tablet at a desk" style="background:linear-gradient(135deg,#5e8fa8,#d8e4ea)"></div>
        <h5>Lorem Ipsum is simply dummy text of the printing.</h5>
        <p>Lorem Ipsum is dummy text of the printing and type setting industry Lorem...</p>
      </article>
      <article class="work-card">
        <div class="work-image" role="img" aria-label="Hand touching a smartphone screen" style="background:linear-gradient(135deg,#a9c6dc,#f1f4f7)"></div>
        <h5>Lorem Ipsum is simply dummy text of the printing.</h5>
        <p>Lorem Ipsum is dummy text of the printing and type setting industry Lorem...</p>
      </article>
      <article class="work-card">
        <div class="work-image" role="img" aria-label="Person working on a tablet at a bright desk" style="background:linear-gradient(135deg,#e9eef2,#7f9fc0)"></div>
        <h5>Lorem Ipsum is simply dummy text of the printing.</h5>
        <p>Lorem Ipsum is dummy text of the printing and type setting industry Lorem...</p>
      </article>
      <article class="work-card">
        <div class="work-image" role="img" aria-label="Hand holding a smartphone showing an app" style="background:linear-gradient(135deg,#f0eeec,#c9a89a)"></div>
        <h5>Lorem Ipsum is simply dummy text of the printing.</h5>
        <p>Lorem Ipsum is dummy text of the printing and type setting industry Lorem...</p>
      </article>
    </div>
  </div>
</section>

<section class="clients">
  <div class="container">
    <h2 class="section-title">WHAT OUR <em>CLIENT SAY</em></h2>
    <div class="client-list">
      <div class="client">
        <div class="client-photo" role="img" aria-label="Portrait of a client" style="background:linear-gradient(160deg,#c9b9a8,#8a6e58)"></div>
        <p>Lorem Ipsum is simply dummy text of the printing and typesetting industry. Lorem Ipsum has been the industry.<span class="name">- Client Name</span></p>
      </div>
      <div class="client">
        <div class="client-photo" role="img" aria-label="Portrait of a client" style="background:linear-gradient(160deg,#d9d2c9,#7a6556)"></div>
        <p>Lorem Ipsum is simply dummy text of the printing and typesetting industry. Lorem Ipsum has been the industry.<span class="name">- Client Name</span></p>
      </div>
    </div>
  </div>
</section>

<footer class="footer">
  <div class="footer-brand"><span class="brand-square"></span><span class="brand-name">QUARRYMIND</span></div>
  <div class="footer-social"><span class="first"></span><span></span><span></span></div>
  <div class="footer-links">
    <a class="active">Home</a><span class="sep">|</span><a>About</a><span class="sep">|</span><a>Services</a><span class="sep">|</span><a>Our Work</a><span class="sep">|</span><a>News</a><span class="sep">|</span><a>Contact</a>
  </div>
  <p class="copyright">© <span>QUARRYMIND</span> - 2016. All Rights Reserved.</p>
</footer>

</body>
</html>
```